Meridel Capra SA Business Cards

Dear all,
Thank you for reading my brief and project. My company is doing doing advisory in real estate and to comapnies + real estates services as asset management, brokerage, development etc.
I would like to get a business card for my company which is clear, professionnal and serious.
Please have a look to the attachement to see the logos of the company

Industry/Entity Type

Real Estate

Contact Information for Business Card

I would like to have in the business card the following
Principal side:
- Logo of the company (or Monogram)
- First and Last Name (Paulo Vestrand)
- Mobile number
- email address

Second side:
- Address (Chemin des Orvets 17, 1226 Thônex - Switzerland)
- website (www.meridelcapra.ch)

Requirements
Must have
• Refer to the typeface and logo colors

```html
<!DOCTYPE html>
<html lang="en">
<head>
<meta charset="utf-8">
<title>Meridel Capra SA Business Cards</title>
<link rel="stylesheet" href="https://fonts.googleapis.com/css2?family=Montserrat:wght@600&family=Roboto:wght@400;500&display=swap">
<style>
  :root {
    --bg: #e8e9eb;
    --slate: #3e4a5b;
    --blue: #1f78c1;
    --ink: #3a4350;
    --white: #ffffff;
  }
  * { margin: 0; padding: 0; box-sizing: border-box; }
  html, body { width: 1200px; height: 900px; overflow: hidden; }
  body {
    background: var(--bg);
    font-family: "Roboto", Arial, sans-serif;
    position: relative;
  }
  .card {
    position: absolute;
    width: 520px;
    height: 320px;
    box-shadow: 0 2px 10px rgba(0,0,0,0.12);
  }
  .card--back { left: 80px; top: 110px; background: var(--slate); color: var(--white); }
  .card--front { left: 600px; top: 470px; background: var(--white); color: var(--ink); }

  .brand {
    position: absolute;
    display: flex;
    align-items: center;
    gap: 14px;
  }
  .brand__mark { width: 30px; height: 30px; }
  .card--back .brand__mark { background: var(--white); }
  .card--front .brand__mark { background: var(--slate); }
  .brand__name {
    font-family: "Montserrat", Arial, sans-serif;
    font-weight: 600;
    font-size: 24px;
    letter-spacing: 1px;
  }
  .card--back .brand__name { color: var(--white); }
  .card--front .brand__name { color: var(--slate); }
  .card--back .brand { left: 90px; top: 90px; }
  .card--front .brand { left: 90px; top: 70px; }

  .rule {
    position: absolute;
    width: 1px;
    transform: rotate(-12deg);
  }

  .back__web {
    position: absolute; left: 0; right: 0; top: 196px;
    display: flex; justify-content: center; align-items: center; gap: 8px;
    font-size: 14px; letter-spacing: 0.3px;
  }
  .back__address {
    position: absolute; left: 0; right: 0; top: 244px;
    text-align: center; font-size: 13.5px; letter-spacing: 0.3px;
  }
  .icon { width: 13px; height: 13px; flex: none; }

  .person {
    position: absolute; left: 60px; top: 176px; text-align: right; width: 190px;
  }
  .person__name { color: var(--blue); font-weight: 500; font-size: 22px; }
  .person__role { font-size: 13.5px; margin-top: 4px; color: var(--ink); }
  .front__divider {
    position: absolute; left: 268px; top: 170px; width: 1px; height: 64px; background: var(--ink);
  }
  .contact {
    position: absolute; left: 288px; top: 178px; list-style: none;
    font-size: 14px; color: var(--ink);
  }
  .contact li { display: flex; align-items: center; gap: 9px; margin-bottom: 10px; }
</style>
</head>
<body>

<section class="card card--back" aria-label="Business card, back side">
  <div class="brand">
    <span class="brand__mark"></span>
    <span class="brand__name">MERIDEL CAPRA</span>
  </div>
  <span class="rule" style="left:74px;top:70px;height:74px;background:rgba(255,255,255,0.7);"></span>
  <p class="back__web">
    <svg class="icon" viewBox="0 0 16 16" aria-hidden="true"><circle cx="8" cy="8" r="7" fill="none" stroke="#fff" stroke-width="1.5"/><path d="M1 8h14M8 1c2.5 2.5 2.5 11.5 0 14M8 1c-2.5 2.5-2.5 11.5 0 14" fill="none" stroke="#fff" stroke-width="1.2"/></svg>
    www.meridelcapra.ch
  </p>
  <p class="back__address">Chemin des Orvets 17, 1226 Thônex - Switzerland</p>
</section>

<section class="card card--front" aria-label="Business card, front side">
  <div class="brand">
    <span class="brand__mark"></span>
    <span class="brand__name">MERIDEL CAPRA</span>
  </div>
  <span class="rule" style="left:74px;top:50px;height:74px;background:var(--blue);"></span>
  <div class="person">
    <p class="person__name">Paulo Vestrand</p>
    <p class="person__role">General Manager</p>
  </div>
  <span class="front__divider"></span>
  <ul class="contact">
    <li>
      <svg class="icon" viewBox="0 0 16 16" aria-hidden="true"><path d="M4 1.5l2.2 3-1.4 1.6c.9 2 2.5 3.6 4.6 4.6l1.6-1.4 3 2.2-1.3 2.5C7 13.8 2.2 9 1.5 3z" fill="#1f78c1"/></svg>
      0412 538 906
    </li>
    <li>
      <svg class="icon" viewBox="0 0 16 16" aria-hidden="true"><rect x="1" y="3" width="14" height="10" rx="1" fill="#1f78c1"/><path d="M1.5 3.8L8 9l6.5-5.2" fill="none" stroke="#fff" stroke-width="1.3"/></svg>
      paulo@meridelcapra.ch
    </li>
  </ul>
</section>

</body>
</html>
```